Parcels & Petals
Parcels & Petals - Gifts and Occasions
Creative Brief
Bright & Fun-filled
Ritu Malhotra
C-17, Dilkusha Marg Lucknow - 226014
ritumal47@postbright.example
www.parcelspetals.example
I want the logo on one side and the other details on the other side. The logo to be used is draft no. 3 in my project parcels and petals

```html
<!DOCTYPE html>
<html lang="en">
<head>
<meta charset="utf-8">
<title>Parcels &amp; Petals – Stationery Set</title>
<link rel="stylesheet" href="https://fonts.googleapis.com/css2?family=Nunito:wght@400;700;800&display=swap">
<style>
  :root {
    --backdrop: #ece9e4;
    --paper: #ffffff;
    --paper-edge: #dcdcdc;
    --brand: #2f9fe0;
    --brand-faint: rgba(47,159,224,0.12);
    --wave-blue: #3aa3e6;
    --wave-green: #7cc242;
    --label: #5a5046;
    --ink: #666;
  }
  * { box-sizing: border-box; margin: 0; padding: 0; }
  html, body { width: 1200px; height: 446px; overflow: hidden; }
  body {
    background: var(--backdrop);
    font-family: "Nunito", sans-serif;
    position: relative;
  }
  .sheet {
    position: absolute;
    background: var(--paper);
    border: 1px solid var(--paper-edge);
    box-shadow: 0 2px 5px rgba(0,0,0,0.12);
    overflow: hidden;
  }
  .label {
    position: absolute;
    font-size: 7px;
    letter-spacing: 0.5px;
    color: var(--label);
    text-transform: uppercase;
    white-space: nowrap;
  }
  .brand-name {
    position: absolute;
    font-weight: 800;
    color: var(--brand);
    line-height: 1;
    white-space: nowrap;
  }
  .brand-name.faint { color: var(--brand-faint); }
  .brand-name.centered { left: 0; right: 0; text-align: center; }
  .watermark {
    left: 0; right: 0;
    top: 128px;
    font-size: 34px;
    line-height: 1.05;
    text-align: center;
    white-space: normal;
  }
  .waves { position: absolute; left: 0; bottom: 0; width: 100%; }
  .small-text {
    position: absolute;
    font-size: 4px;
    color: var(--ink);
    line-height: 1.4;
  }

  /* business cards */
  .card-front { left: 19px; top: 216px; width: 113px; height: 48px; }
  .card-back  { left: 19px; top: 302px; width: 113px; height: 48px; }

  /* letterheads */
  .letterhead { top: 19px; width: 252px; height: 365px; }
  .letterhead.one { left: 156px; }
  .letterhead.two { left: 475px; }

  /* envelopes */
  .envelope { left: 792px; width: 396px; }
  .envelope .flap { position: absolute; left: 0; top: 0; width: 100%; }
  .env-blue  { top: 12px;  height: 72px; }
  .env-green { top: 91px;  height: 113px; }
  .env-white { top: 187px; height: 113px; }
  .env-front { left: 792px; top: 264px; width: 264px; height: 120px; }
</style>
</head>
<body>

  <!-- business cards -->
  <div class="label" style="left:8px; top:170px;">Business Card Design</div>

  <div class="sheet card-front">
    <div class="brand-name centered" style="top:10px; font-size:12px;">Parcels &amp; Petals</div>
    <svg class="waves" viewBox="0 0 113 14" height="14" preserveAspectRatio="none" aria-hidden="true">
      <path d="M0 6 Q40 14 113 2 L113 14 L0 14Z" fill="var(--wave-green)"/>
      <path d="M0 10 Q50 14 113 6 L113 14 L0 14Z" fill="var(--wave-blue)"/>
    </svg>
  </div>
  <div class="label" style="left:19px; top:270px;">Business Card Front</div>

  <div class="sheet card-back">
    <div class="brand-name" style="left:6px; top:6px; font-size:8px;">Parcels &amp; Petals</div>
    <div class="small-text" style="left:6px; top:17px;">
      Ritu Malhotra<br>
      C-17, Dilkusha Marg Lucknow - 226014<br>
      ritumal47@postbright.example<br>
      www.parcelspetals.example
    </div>
    <svg class="waves" viewBox="0 0 113 10" height="10" preserveAspectRatio="none" aria-hidden="true">
      <path d="M0 4 Q40 10 113 2 L113 10 L0 10Z" fill="var(--wave-green)"/>
      <path d="M0 8 Q50 10 113 5 L113 10 L0 10Z" fill="var(--wave-blue)"/>
    </svg>
  </div>
  <div class="label" style="left:19px; top:358px;">Business Card Back</div>

  <!-- letterheads -->
  <div class="sheet letterhead one">
    <div class="brand-name" style="left:22px; top:20px; font-size:15px;">Parcels &amp; Petals</div>
    <div class="small-text" style="right:20px; top:22px; text-align:right;">
      ritumal47@postbright.example<br>www.parcelspetals.example
    </div>
    <div class="brand-name faint watermark">Parcels &amp;<br>Petals</div>
    <svg class="waves" viewBox="0 0 252 40" height="40" preserveAspectRatio="none" aria-hidden="true">
      <path d="M0 18 Q110 40 252 10 L252 40 L0 40Z" fill="var(--wave-green)"/>
      <path d="M0 26 Q120 42 252 18 L252 40 L0 40Z" fill="var(--wave-blue)"/>
    </svg>
  </div>
  <div class="label" style="left:240px; top:396px;">Letter Head Option 1</div>

  <div class="sheet letterhead two">
    <div class="brand-name" style="left:22px; top:20px; font-size:15px;">Parcels &amp; Petals</div>
    <div class="brand-name faint watermark">Parcels &amp;<br>Petals</div>
    <div class="small-text" style="left:0; right:0; bottom:44px; text-align:center;">
      C-17, Dilkusha Marg Lucknow - 226014 · ritumal47@postbright.example · www.parcelspetals.example
    </div>
    <svg class="waves" viewBox="0 0 252 40" height="40" preserveAspectRatio="none" aria-hidden="true">
      <path d="M0 14 Q130 40 252 12 L252 40 L0 40Z" fill="var(--wave-green)"/>
      <path d="M0 22 Q130 44 252 20 L252 40 L0 40Z" fill="var(--wave-blue)"/>
    </svg>
  </div>
  <div class="label" style="left:560px; top:396px;">Letter Head Option 2</div>

  <!-- envelopes -->
  <div class="sheet envelope env-blue">
    <svg class="flap" viewBox="0 0 396 72" height="72" preserveAspectRatio="none" aria-hidden="true">
      <path d="M0 0 H396 V40 Q198 72 0 40Z" fill="var(--wave-blue)"/>
    </svg>
  </div>

  <div class="sheet envelope env-green">
    <svg class="flap" viewBox="0 0 396 70" height="70" preserveAspectRatio="none" aria-hidden="true">
      <path d="M0 0 H396 V24 L320 60 Q198 76 76 60 L0 24Z" fill="var(--wave-green)"/>
    </svg>
  </div>

  <div class="sheet envelope env-white">
    <svg class="flap" viewBox="0 0 396 70" height="70" preserveAspectRatio="none" aria-hidden="true">
      <path d="M0 0 H396 V24 L320 60 Q198 76 76 60 L0 24Z" fill="none" stroke="var(--paper-edge)"/>
    </svg>
    <div class="brand-name faint" style="left:240px; top:42px; font-size:13px;">Parcels &amp; Petals</div>
  </div>

  <div class="sheet env-front">
    <div class="brand-name" style="left:12px; top:12px; font-size:11px;">Parcels &amp; Petals</div>
    <div class="brand-name faint centered" style="top:46px; font-size:20px;">Parcels &amp; Petals</div>
    <svg class="waves" viewBox="0 0 264 24" height="24" preserveAspectRatio="none" aria-hidden="true">
      <path d="M0 10 Q120 26 264 4 L264 24 L0 24Z" fill="var(--wave-green)"/>
      <path d="M0 16 Q130 26 264 10 L264 24 L0 24Z" fill="var(--wave-blue)"/>
    </svg>
  </div>
  <div class="label" style="left:1000px; top:396px;">Envelope Design</div>

</body>
</html>
```